Author needs design for self-help relationship book

I need a book cover design for a self-help handbook on relationships called 'Where Partners Find Calm Harbours - Letters From Quiet Mornings". The design should appeal in the main to young couples anywhere in the world.

```html
<!DOCTYPE html>
<html lang="en">
<head>
<meta charset="utf-8">
<title>Where Partners Find Calm Harbours – Book Cover</title>
<link rel="stylesheet" href="https://fonts.googleapis.com/css2?family=Archivo:wdth,wght@62..125,400;62..125,500&display=swap">
<style>
  :root {
    --cover-orange: #f39c0c;
    --cover-orange-light: #f7a21a;
    --cover-amber-deep: #a85a08;
    --cover-amber-mid: #c97409;
    --title-white: #ffffff;
    --author-red: #a3150e;
  }
  html, body {
    margin: 0;
    padding: 0;
    width: 800px;
    height: 1200px;
    overflow: hidden;
    background: var(--cover-orange);
  }
  .book-cover {
    position: relative;
    width: 800px;
    height: 1200px;
    overflow: hidden;
    background: var(--cover-orange);
  }
  .cover-photo {
    position: absolute;
    inset: 0;
    background:
      radial-gradient(ellipse 200px 360px at 430px 480px, rgba(168, 90, 8, 0.55), rgba(168, 90, 8, 0) 100%),
      radial-gradient(ellipse 260px 600px at 420px 700px, rgba(201, 116, 9, 0.45), rgba(201, 116, 9, 0) 100%),
      linear-gradient(100deg, var(--cover-orange-light) 0%, var(--cover-orange) 55%, #e48a06 100%);
  }
  .cover-title {
    position: absolute;
    left: 0;
    right: 0;
    top: 300px;
    margin: 0;
    text-align: center;
    font-family: "Archivo", "Helvetica Neue", Arial, sans-serif;
    font-stretch: 115%;
    font-weight: 500;
    font-size: 37px;
    letter-spacing: 0.14em;
    line-height: 117px;
    color: var(--title-white);
  }
  .cover-title .title-line {
    display: block;
    height: 117px;
    line-height: 52px;
  }
  .cover-author {
    position: absolute;
    left: 0;
    right: 0;
    top: 1092px;
    margin: 0;
    text-align: center;
    font-family: "Archivo", "Helvetica Neue", Arial, sans-serif;
    font-stretch: 115%;
    font-weight: 500;
    font-size: 32px;
    letter-spacing: 0.2em;
    color: var(--author-red);
  }
</style>
</head>
<body>
  <main class="book-cover">
    <div class="cover-photo" role="img" aria-label="Soft-focus photograph of a couple embracing, seen as a blurred silhouette behind an orange veil"></div>
    <h1 class="cover-title">
      <span class="title-line">Where</span>
      <span class="title-line">Partners Find</span>
      <span class="title-line">Calm Harbours</span>
      <span class="title-line">- Letters From</span>
      <span class="title-line">Quiet Mornings</span>
    </h1>
    <p class="cover-author">AUTHOR NAME</p>
  </main>
</body>
</html>
```